The Fernbrook Laundromat - Pre-Opening Marketing Postcard

We need a design for a 6"x11" postcard that we will use to advertise the upcoming opening of a new laundromat in Halden, NY. The name of the store is "The Fernbrook Laundromat", and the most important things are: match the colors on the card to our logo colors, but also add in some yellow and possibly red accents; say "Free Dryers" in a big, obvious way; include generic washer/dryer pictures, put a basic map of the location on the back of the card, and leave the right 1/3 of the card blank except for the retail indicia and the name "Local Postal Customer". Please refer to the uploaded file showing an example basic layout for the card.
Target Market(s)
low-to-middle-income residents within a 3-mile radius
Industry/Entity Type
Retail
Requirements
Must have
- - The words FREE DRYERS!
- - A simple, hand-drawn map of the location (412 Ashgrove Road, Halden, NY) and major roads nearby (dorset avenue, ashgrove road, elm ave, etc.)
- - The words Opening Soon! (or Opening in March!)
- - The words Newly-Built Laundromat, or New Store!, or something similar
- - The words Local Postal Customer on the back, as shown in my example design layout
- - The retail indicia positioned as shown in my example design layout
- - nothing else on the rear, right-hand 1/3 of the card other than local postal customer and the indicia
Nice to have
- - A transparent background using the generic washers and/or generic dryers pictures
- - Some yellow and red accents or colors to appeal to our hispanic customers
- - The words Professional Wash & Fold Service
Should not have
- - Anything on the back, right-hand 1/3 of the card other than Local Postal Customer and the retail indicia picture

```html
<!DOCTYPE html>
<html lang="en">
<head>
<meta charset="utf-8">
<title>The Fernbrook Laundromat – Opening Postcard</title>
<link rel="stylesheet" href="https://fonts.googleapis.com/css2?family=Montserrat:wght@600;800;900&family=Roboto+Condensed:wght@400;700&family=Roboto:wght@400;700&display=swap">
<style>
  :root{
    --blue-deep:#174f96;
    --blue-mid:#2a72bd;
    --blue-bright:#3c92d6;
    --navy-text:#1f4d95;
    --logo-disc:#bfe0e0;
    --accent-yellow:#fff200;
    --accent-red:#d22a2a;
    --pill-fill:#a9d8f2;
    --band-light:#f4f5f7;
    --band-shade:#d3d6db;
    --paper:#ffffff;
    --ink:#111111;
    --stage:#ece9e4;
  }
  *{margin:0;padding:0;box-sizing:border-box}
  html,body{width:1200px;height:1000px;overflow:hidden;background:var(--stage)}
  .card{position:absolute;overflow:hidden;box-shadow:0 4px 14px rgba(0,0,0,.25)}
  .card svg.card-art{position:absolute;inset:0}
  .card-front{left:52px;top:38px;width:796px;height:432px}
  .card-back{left:338px;top:506px;width:794px;height:432px;background:var(--paper)}

  .logo-name{position:absolute;display:flex;flex-direction:column;align-items:center;justify-content:center;text-align:center;
    font-family:"Roboto Condensed",sans-serif;font-weight:700;color:var(--navy-text);line-height:1.02}
  .front-logo{left:28px;top:50px;width:320px;height:300px;font-size:46px}
  .back-logo{left:50px;top:270px;width:116px;height:108px;font-size:17px}

  .headline{position:absolute;left:402px;top:66px;width:364px;text-align:center;
    font-family:"Montserrat",sans-serif;font-weight:900;font-size:75px;line-height:.88;color:var(--accent-yellow);letter-spacing:-1px}
  .opening-pill{position:absolute;left:422px;top:233px;width:314px;height:45px;border:2px solid var(--accent-red);border-radius:5px;
    background:var(--pill-fill);font-family:"Montserrat",sans-serif;font-weight:600;font-size:26px;color:var(--navy-text);
    display:flex;align-items:center;justify-content:center;white-space:nowrap}
  .opening-pill strong{color:var(--accent-red);font-weight:800;margin-left:8px}

  .front-footer{position:absolute;left:8px;right:0;top:384px;display:flex;align-items:center;gap:6px;white-space:nowrap;
    font-family:"Roboto Condensed",sans-serif;font-size:23px;color:var(--navy-text)}
  .front-footer .rule{height:2px;background:var(--navy-text)}

  .map-area{position:absolute;left:50px;top:19px;width:349px;height:224px;background:var(--paper);padding:6px}
  .map-area div{width:100%;height:100%;background:linear-gradient(135deg,#e6e6e8,#d9dadd)}
  .service-block{position:absolute;left:210px;top:306px;width:200px;color:var(--paper)}
  .service-title{font-family:"Montserrat",sans-serif;font-weight:800;font-size:14.5px;line-height:1.1;padding-bottom:5px;border-bottom:1px solid rgba(255,255,255,.8)}
  .service-address{font-family:"Roboto Condensed",sans-serif;font-size:15px;margin-top:6px;white-space:nowrap}

  .recipient{position:absolute;left:540px;top:205px;width:160px;transform:rotate(90deg);
    font-family:Arial,"Roboto",sans-serif;font-size:21px;line-height:1.1;color:var(--ink);text-align:left}
  .indicia{position:absolute;left:702px;top:358px;width:80px;transform:rotate(90deg);
    font-family:"Roboto",Arial,sans-serif;font-weight:700;font-size:7.5px;line-height:1.25;color:var(--ink);text-align:center}
</style>
</head>
<body>

<section class="card card-front" aria-label="Postcard front">
  <svg class="card-art" width="796" height="432" viewBox="0 0 796 432">
    <defs>
      <linearGradient id="frontSky" x1="0" y1="0" x2="1" y2="1">
        <stop offset="0" stop-color="#2c7ac4"/><stop offset="1" stop-color="#1b5aa5"/>
      </linearGradient>
      <linearGradient id="washerTone" x1="0" y1="0" x2="1" y2="0">
        <stop offset="0" stop-color="#2a6fb7" stop-opacity="0"/>
        <stop offset=".4" stop-color="#4d88c2" stop-opacity=".55"/>
        <stop offset="1" stop-color="#3a78b8" stop-opacity=".75"/>
      </linearGradient>
      <linearGradient id="bandTone" x1="0" y1="0" x2="0" y2="1">
        <stop offset="0" stop-color="#ffffff"/><stop offset="1" stop-color="#d3d6db"/>
      </linearGradient>
    </defs>
    <rect width="796" height="432" fill="url(#frontSky)"/>
    <rect x="360" y="0" width="436" height="370" fill="url(#washerTone)" role="img" aria-label="Row of front-loading washers and dryers in a laundromat"/>
    <path d="M0,298 C160,290 330,372 520,356 C650,345 730,322 796,318 L796,432 L0,432Z" fill="var(--accent-red)"/>
    <path d="M0,322 C170,318 330,392 520,380 C650,372 730,348 796,344 L796,432 L0,432Z" fill="url(#bandTone)"/>
    <circle cx="188" cy="202" r="172" fill="var(--logo-disc)"/>
  </svg>
  <div class="logo-name front-logo">The Fernbrook<br>Laundromat</div>
  <div class="headline">FREE<br>DRYERS!</div>
  <div class="opening-pill">Opening in<strong>March!</strong></div>
  <div class="front-footer">
    <span class="rule" style="width:58px"></span>
    <span>Newly-Built Laundromat</span>
    <span class="rule" style="width:140px"></span>
    <span>412 Ashgrove Road, Halden, NY</span>
    <span class="rule" style="flex:1"></span>
  </div>
</section>

<section class="card card-back" aria-label="Postcard back">
  <svg class="card-art" width="794" height="432" viewBox="0 0 794 432">
    <defs>
      <linearGradient id="backSky" x1="0" y1="1" x2="1" y2="0">
        <stop offset="0" stop-color="#1b58a3"/><stop offset="1" stop-color="#3d98da"/>
      </linearGradient>
    </defs>
    <rect width="794" height="432" fill="url(#backSky)"/>
    <path d="M446,0 C414,140 472,200 438,300 C422,350 432,400 446,432 L794,432 L794,0Z" fill="var(--accent-red)"/>
    <path d="M460,0 C428,140 486,200 452,300 C436,350 446,400 460,432 L794,432 L794,0Z" fill="var(--paper)"/>
    <circle cx="107" cy="324" r="60" fill="var(--logo-disc)"/>
  </svg>
  <div class="map-area"><div role="img" aria-label="Street map showing 412 Ashgrove Road near Dorset Avenue and Elm Ave"></div></div>
  <div class="logo-name back-logo">The Fernbrook<br>Laundromat</div>
  <div class="service-block">
    <div class="service-title">PROFESSIONAL WASH<br>&amp; FOLD SERVICE</div>
    <div class="service-address">412 Ashgrove Road, Halden, NY</div>
  </div>
  <div class="recipient">Local Postal<br>Customer</div>
  <div class="indicia">PRSRT STD<br>ECRWSS<br>U.S. POSTAGE<br>PAID<br>EDDM-Retail</div>
</section>

</body>
</html>
```